Gentleman's grooming products require a business card

I need a business card that incorporates the logo [ or parts of ] that we had Pixel Hive design for us as uploaded.

We sell online, mens grooming products including moustache waxes, beard oils and shaving accessories.
We want a card that is classy, professional and a card that shouts mens products.

Target Market(s)

Young professional male market

Industry/Entity Type

Business

Contact Information for Business Card

Ross and Edith Carwell
Lather and Lore
Purveyors of gentleman's stiffeners and grooming requisites
M :0418529647
E : ross@latherandlore.com.au
E : edith@latherandlore.com.au
E : sales@theblokesbalmery.com.au

W : www.latherandlore.com.au

Requirements
Must have
• Class
Nice to have
• Professionalism

```html
<!DOCTYPE html>
<html lang="en">
<head>
<meta charset="utf-8">
<title>Lather and Lore – Business Card</title>
<link rel="stylesheet" href="https://fonts.googleapis.com/css2?family=Cormorant+SC:wght@500&family=Open+Sans:wght@400&display=swap">
<style>
  :root {
    --backdrop: #a9a9a9;
    --card: #f4f4f4;
    --panel: #0b0b0b;
    --ink-light: #f2f2f2;
    --ink-soft: #cfcfcf;
    --rivet: #e9e9e9;
  }
  * { box-sizing: border-box; margin: 0; padding: 0; }
  html, body { width: 1200px; height: 750px; overflow: hidden; }
  body {
    background: linear-gradient(#999 0%, var(--backdrop) 100%);
    display: flex; align-items: center; justify-content: center;
  }
  .card {
    position: relative;
    width: 700px; height: 400px;
    background: var(--card);
    border-radius: 30px;
    box-shadow: 0 12px 30px rgba(0,0,0,.25);
  }
  .panel {
    position: absolute;
    background: var(--panel);
    color: var(--ink-light);
  }
  .panel::before, .panel::after,
  .panel .rivets::before, .panel .rivets::after {
    content: ""; position: absolute;
    width: 10px; height: 10px; border-radius: 50%;
    background: var(--rivet);
  }
  .panel::before { top: 9px; left: 9px; }
  .panel::after { top: 9px; right: 9px; }
  .panel .rivets::before { bottom: 9px; left: 9px; }
  .panel .rivets::after { bottom: 9px; right: 9px; }

  .brand-panel { left: 30px; top: 30px; width: 345px; height: 340px; }
  .brand {
    position: absolute; left: 30px; right: 30px; top: 110px;
    text-align: center;
  }
  .brand-mark {
    width: 34px; height: 34px; margin: 0 auto 8px;
    border: 1.5px solid var(--ink-light);
  }
  .brand-name {
    font-family: "Cormorant SC", serif; font-weight: 500;
    font-size: 40px; line-height: 1; letter-spacing: 1px;
    color: var(--ink-light);
    border-bottom: 1px solid var(--ink-soft);
    padding-bottom: 6px;
  }
  .brand-tagline {
    margin-top: 6px;
    font-family: "Cormorant SC", serif; font-weight: 500;
    font-size: 9.5px; letter-spacing: .6px; color: var(--ink-soft);
  }

  .name-panel { left: 390px; top: 30px; width: 280px; height: 100px; }
  .owners {
    position: absolute; left: 0; right: 0; top: 32px; text-align: center;
    font-family: "Cormorant SC", serif; font-weight: 500;
  }
  .owners-name { font-size: 19px; letter-spacing: .5px; }
  .owners-company { font-size: 11px; color: var(--ink-soft); margin-top: 3px; letter-spacing: .8px; }

  .contact-panel { left: 390px; top: 140px; width: 280px; height: 230px; }
  .contacts {
    list-style: none; position: absolute; left: 28px; top: 54px;
    font-family: "Open Sans", sans-serif; font-size: 11.5px; color: var(--ink-light);
  }
  .contacts li { display: flex; align-items: center; gap: 8px; height: 24px; }
  .contacts svg { width: 14px; height: 14px; flex: none; }
</style>
</head>
<body>
  <article class="card">
    <section class="panel brand-panel">
      <span class="rivets"></span>
      <div class="brand">
        <div class="brand-mark"></div>
        <div class="brand-name">Lather and Lore</div>
        <div class="brand-tagline">Purveyors of gentleman's stiffeners and grooming requisites</div>
      </div>
    </section>

    <section class="panel name-panel">
      <span class="rivets"></span>
      <div class="owners">
        <div class="owners-name">Ross and Edith Carwell</div>
        <div class="owners-company">Lather and Lore</div>
      </div>
    </section>

    <section class="panel contact-panel">
      <span class="rivets"></span>
      <ul class="contacts">
        <li>
          <svg viewBox="0 0 14 14" fill="none" stroke="#f2f2f2" stroke-width="1"><circle cx="7" cy="7" r="6.3"/><path d="M4.6 4c.4 2.6 2.6 5 5.4 5.6l.6-1.2-1.4-.8-.7.7C7.5 7.8 6.4 6.7 6 5.7l.7-.7-.8-1.4z" fill="#f2f2f2" stroke="none"/></svg>
          0418529647
        </li>
        <li>
          <svg viewBox="0 0 14 14" fill="none" stroke="#f2f2f2" stroke-width="1"><circle cx="7" cy="7" r="6.3"/><rect x="3.8" y="4.8" width="6.4" height="4.4"/><path d="M3.8 4.8 7 7.3l3.2-2.5"/></svg>
          ross@latherandlore.com.au
        </li>
        <li>
          <svg viewBox="0 0 14 14" fill="none" stroke="#f2f2f2" stroke-width="1"><circle cx="7" cy="7" r="6.3"/><rect x="3.8" y="4.8" width="6.4" height="4.4"/><path d="M3.8 4.8 7 7.3l3.2-2.5"/></svg>
          edith@latherandlore.com.au
        </li>
        <li>
          <svg viewBox="0 0 14 14" fill="none" stroke="#f2f2f2" stroke-width="1"><circle cx="7" cy="7" r="6.3"/><rect x="3.8" y="4.8" width="6.4" height="4.4"/><path d="M3.8 4.8 7 7.3l3.2-2.5"/></svg>
          sales@theblokesbalmery.com.au
        </li>
        <li>
          <svg viewBox="0 0 14 14" fill="none" stroke="#f2f2f2" stroke-width="1"><circle cx="7" cy="7" r="6.3"/><circle cx="7" cy="7" r="3.4"/><ellipse cx="7" cy="7" rx="1.4" ry="3.4"/><path d="M3.6 7h6.8"/></svg>
          www.latherandlore.com.au
        </li>
      </ul>
    </section>
  </article>
</body>
</html>
```